Pilates trainer needs new website

Summary: I need a new, meaningful website in a 1-page format, but one that can be expanded if necessary. I teach in various studios and in the future also in companies. Therefore, the website should convey growth, joy, uniqueness, workout and a bit of luxury.
The website should be inviting.
Layout:
Introduction what I offer
A bit about me
Option to upload price list and timetable in PDF format
Studio address where I teach
The color scheme should be petrol, gold, and colors that match. Not too dark, please.
My current website www.movewell-brennach.de, new domain is corebalance-studio.com (I have already purchased it)
Logo file attached
I have attached a few suggestions but I am also happy to be surprised.

Target Market(s)

Pilates private and small groups,

Industry/Entity Type

Pilates teacher freelancer

Coding

Coded - Design and coding required

Number of Pages Required

1 page

Requirements
Must have
• Welcoming appearance, about me, pictures, offers, colors from the logo but don't get do dark, more fresh and a bit luxurious
Should not have
• Not too wild and going crazy with colors

```html
<!DOCTYPE html>
<html lang="en">
<head>
<meta charset="utf-8">
<title>Core Balance – Pilates Studio Trainer</title>
<link href="https://fonts.googleapis.com/css2?family=Great+Vibes&family=Inter:wght@400;500;600;700&family=Lora:wght@400;500&display=swap" rel="stylesheet">
<style>
:root{
  --petrol:#19ab9a;
  --gold:#c59654;
  --gold-soft:#fde8cc;
  --ink:#1a1a1a;
  --muted:#9a9a9a;
  --field:#efefef;
  --footer:#1c2726;
  --white:#ffffff;
}
*{box-sizing:border-box;margin:0;padding:0}
html,body{width:1200px;height:3552px;overflow:hidden}
body{position:relative;background:var(--white);font-family:"Inter",sans-serif;color:var(--ink)}
.abs{position:absolute}
.center{left:0;width:1200px;text-align:center}
.eyebrow{font-family:"Lora",serif;font-size:15px;letter-spacing:3.5px;text-transform:uppercase;color:var(--ink)}
.script{font-family:"Great Vibes",cursive;font-weight:400;color:var(--ink);line-height:1}
.btn{display:flex;align-items:center;justify-content:center;color:var(--white);font-size:12.5px;text-transform:uppercase;letter-spacing:.3px}
.btn-gold{background:var(--gold)}
.btn-petrol{background:var(--petrol)}

/* header */
.brand{top:34px;left:0;width:1200px;display:flex;justify-content:center;align-items:center;gap:10px;font-size:22px;font-weight:600;color:var(--petrol)}
.brand-dot{width:18px;height:18px;border-radius:50%;background:var(--petrol)}
.header-line{top:132px;left:0;width:1200px;height:1px;background:#e9efee}
.nav{top:150px;left:0;width:1200px;display:flex;justify-content:center;gap:42px;font-size:13px;text-transform:uppercase}
.nav .active{font-weight:600}
.nav .lang{display:flex;align-items:center;gap:8px}

/* hero */
.hero{top:186px;left:0;width:1200px;height:458px;
  background:linear-gradient(100deg,#8a6a4c 0%,#5e4634 22%,#a58767 40%,#6b513d 60%,#9d7f62 80%,#5a4332 100%);
  clip-path:polygon(0 0,100% 0,100% 361px,50% 458px,0 361px)}
.hero-tag{top:306px;font-size:16.5px;letter-spacing:4px;color:var(--white)}
.hero-title{top:332px;font-size:80px;color:var(--white)}
.hero-sub{top:423px;font-size:25px;letter-spacing:5px;color:var(--white)}
.hero-btn{top:485px;left:465px;width:270px;height:39px;font-size:13px}

/* offer */
.offer-eyebrow{top:712px}
.offer-title{top:740px;font-size:60px}
.benefit{width:250px;text-align:center;font-size:15px;font-weight:600;line-height:20px}
.benefit .icon{width:57px;height:57px;margin:0 auto 19px;background:var(--gold-soft);border:1px solid #f3d3a7;display:flex;align-items:center;justify-content:center}

/* about */
.about{top:1156px;left:0;width:1200px;height:474px;background:var(--gold-soft)}
.about-frame{top:1205px;left:91px;width:447px;height:346px;background:var(--gold)}
.about-photo{top:1233px;left:120px;width:445px;height:346px;background:linear-gradient(135deg,#d9c7ae 0%,#b4916a 45%,#2a2c44 75%,#8d6a47 100%)}
.about-dash{top:1246px;left:133px;width:419px;height:322px;border:1.5px dashed #2a2a2a}
.about-eyebrow{top:1234px;left:633px}
.about-title{top:1262px;left:633px;font-size:52px}
.about-text{top:1332px;left:633px;width:475px;font-size:11.5px;line-height:20px;text-align:justify;color:#222}
.about-btn{top:1516px;left:633px;width:124px;height:37px;font-size:11.5px}

/* pricelist */
.price-eyebrow{top:1697px}
.price-title{top:1726px;font-size:52px}
.slide-side{top:1862px;width:243px;height:400px;opacity:.55}
.slide-left{left:91px;background:linear-gradient(90deg,#ded7cc,#c9b79f 50%,#e8e1d6)}
.slide-right{left:866px;background:linear-gradient(90deg,#e6ded2,#c7ab8a 50%,#ece5db)}
.slide-main{top:1811px;left:334px;width:532px;height:499px;background:linear-gradient(160deg,#e3dcd2 0%,#cfbfa9 35%,#a37a52 60%,#d8cab6 85%,#efe8de 100%)}
.slide-caption{top:2158px;left:334px;width:532px;height:110px;background:rgba(176,130,70,.85);color:var(--white);text-align:center}
.slide-caption h3{margin-top:24px;font-size:27px;font-weight:600}
.slide-caption p{margin-top:8px;font-size:16px}
.slide-arrow{top:2200px}
.price-btn{top:2340px;left:510px;width:180px;height:39px;font-size:11.5px}

/* locations */
.loc-eyebrow{top:2446px}
.loc-title{top:2474px;font-size:56px}
.loc-card{top:2561px;width:499px;height:156px;background:var(--petrol);color:var(--white);text-align:center;display:flex;flex-direction:column;justify-content:center}
.loc-card h3{font-family:"Great Vibes",cursive;font-weight:400;font-size:31px;margin-bottom:8px}
.loc-card p{font-size:16px;line-height:25px}

/* contact */
.contact-eyebrow{top:2785px}
.contact-title{top:2815px;font-size:56px}
.field{background:var(--field);color:var(--muted);font-size:13px;padding:0 25px;display:flex;align-items:center}
.field-area{align-items:flex-start;padding-top:20px}
.send-btn{top:3129px;left:542px;width:116px;height:39px;font-size:12px}

/* footer */
.footer{top:3234px;left:0;width:1200px;height:318px;background:var(--footer)}
.badge{top:3285px;left:91px;width:120px;height:142px;background:#5077a4;border-radius:3px}
.f-head{top:3284px;font-size:16px;font-weight:600;color:var(--white)}
.f-list{font-size:13px;line-height:26px;color:var(--white)}
.f-input{top:3318px;left:758px;width:349px;height:44px;background:#253130;color:#9aa3a2;font-size:13px;padding:0 25px;display:flex;align-items:center}
.f-btn{top:3376px;left:758px;width:130px;height:37px;font-size:13px;text-transform:none}
.f-rule{top:3483px;left:91px;width:1016px;height:1px;background:#4c5756}
.copy{top:3511px;left:91px;font-size:10px;color:var(--white)}
.social{top:3506px;width:25px;height:25px;border-radius:50%;background:var(--petrol)}
</style>
</head>
<body>

<!-- header -->
<div class="abs brand"><span class="brand-dot"></span>Core Balance</div>
<div class="abs header-line"></div>
<nav class="abs nav">
  <span class="active">Home</span>
  <span>Individual Training</span>
  <span>Group Training</span>
  <span>About Us</span>
  <span>Contact Us</span>
  <span class="lang">EN
    <svg width="12" height="8" viewBox="0 0 12 8"><path d="M1 1l5 5 5-5" fill="none" stroke="#1a1a1a" stroke-width="1.8"/></svg>
  </span>
</nav>

<!-- hero -->
<div class="abs hero" role="img" aria-label="Blurred photo of a group pilates class on reformer machines"></div>
<div class="abs center hero-tag">CHANGE HAPPENS THROUGH MOVEMENT AND MOVEMENT HEALS</div>
<div class="abs center script hero-title">Core Balance</div>
<div class="abs center hero-sub">PILATES STUDIO TRAINER</div>
<div class="abs btn btn-gold hero-btn">Request an appointment now</div>

<!-- offer -->
<div class="abs center eyebrow offer-eyebrow">What we offer</div>
<div class="abs center script offer-title">Discover The Benefits</div>

<div class="abs benefit" style="top:827px;left:147px">
  <div class="icon" role="img" aria-label="Fitness icon"><svg width="30" height="30" viewBox="0 0 30 30" fill="none" stroke="#c59654" stroke-width="1.5"><circle cx="15" cy="8" r="3"/><path d="M15 11v9M9 15h12M15 20l-4 7M15 20l4 7"/></svg></div>
  Physical fitness</div>
<div class="abs benefit" style="top:827px;left:475px">
  <div class="icon" role="img" aria-label="Dumbbell icon"><svg width="30" height="30" viewBox="0 0 30 30" fill="none" stroke="#c59654" stroke-width="1.5"><rect x="4" y="9" width="4" height="12"/><rect x="22" y="9" width="4" height="12"/><path d="M8 15h14M2 13v4M28 13v4"/></svg></div>
  A consistently well-trained body</div>
<div class="abs benefit" style="top:827px;left:803px">
  <div class="icon" role="img" aria-label="Mind icon"><svg width="30" height="30" viewBox="0 0 30 30" fill="none" stroke="#c59654" stroke-width="1.5"><circle cx="15" cy="13" r="8"/><path d="M11 21v6h8v-6M12 13h6M15 10v6"/></svg></div>
  Full possession of mental powers</div>
<div class="abs benefit" style="top:979px;left:147px">
  <div class="icon" role="img" aria-label="Posture icon"><svg width="30" height="30" viewBox="0 0 30 30" fill="none" stroke="#c59654" stroke-width="1.5"><rect x="4" y="4" width="22" height="22"/><path d="M10 4v22M20 4v22M4 12h22"/></svg></div>
  Optimal performance of the musculoskeletal system</div>
<div class="abs benefit" style="top:979px;left:475px">
  <div class="icon" role="img" aria-label="Endurance icon"><svg width="30" height="30" viewBox="0 0 30 30" fill="none" stroke="#c59654" stroke-width="1.5"><rect x="6" y="12" width="6" height="14" rx="2"/><rect x="18" y="12" width="6" height="14" rx="2"/><path d="M9 12V6M21 12V6M15 4v6"/></svg></div>
  Flexibility and endurance without risk of injury</div>
<div class="abs benefit" style="top:979px;left:803px">
  <div class="icon" role="img" aria-label="Balance icon"><svg width="30" height="30" viewBox="0 0 30 30" fill="none" stroke="#c59654" stroke-width="1.5"><path d="M5 10c5-6 15-6 20 0M5 20c5 6 15 6 20 0"/><circle cx="15" cy="15" r="4"/></svg></div>
  Minimum effort, maximum success</div>

<!-- about -->
<section class="abs about"></section>
<div class="abs about-frame"></div>
<div class="abs about-photo" role="img" aria-label="Photo of the trainer seated beside a pilates reformer in the studio"></div>
<div class="abs about-dash"></div>
<div class="abs eyebrow about-eyebrow">Little bit about</div>
<div class="abs script about-title">Core Balance</div>
<p class="abs about-text">After discovering my passion for Pilates years ago, I embarked on a journey to become a certified instructor, completing rigorous training with Flow Forward, Core Method Academy, and Northline Pilates. As a member of the National Pilates Guild, I consistently pursue further education to deepen my expertise. My teaching approach emphasizes precision and enjoyment, focusing on small group or individual sessions to ensure optimal support. Beyond Pilates, I enjoy outdoor activities like hiking, skiing, and bouldering, as well as practicing yoga and paddleboarding in the summer.</p>
<div class="abs btn btn-gold about-btn">Learn more</div>

<!-- pricelist -->
<div class="abs center eyebrow price-eyebrow">Our pricelist</div>
<div class="abs center script price-title">Select Your Preference</div>
<div class="abs slide-side slide-left" role="img" aria-label="Photo of a pilates exercise on a reformer"></div>
<div class="abs slide-side slide-right" role="img" aria-label="Photo of a stretching exercise on a reformer"></div>
<div class="abs slide-main" role="img" aria-label="Photo of two women training on pilates reformers"></div>
<div class="abs slide-caption">
  <h3>Individual/Duet Training</h3>
  <p>Start from 85,00€</p>
</div>
<svg class="abs slide-arrow" style="left:362px" width="18" height="26" viewBox="0 0 18 26"><path d="M14 3L5 13l9 10" fill="none" stroke="#fff" stroke-width="3"/></svg>
<svg class="abs slide-arrow" style="left:820px" width="18" height="26" viewBox="0 0 18 26"><path d="M4 3l9 10-9 10" fill="none" stroke="#fff" stroke-width="3"/></svg>
<div class="abs btn btn-gold price-btn">Download pricelist</div>

<!-- locations -->
<div class="abs center eyebrow loc-eyebrow">Our location</div>
<div class="abs center script loc-title">Studio Address Where I Teach</div>
<div class="abs loc-card" style="left:91px">
  <h3>Studio Address Brennach</h3>
  <p>Lindenweg 7 83690 Brennach<br>Entrance around the corner, 2nd floor</p>
</div>
<div class="abs loc-card" style="left:608px">
  <h3>Studio Address Auenfeld</h3>
  <p>Marktstrasse 18 82031 Auenfeld</p>
</div>

<!-- contact -->
<div class="abs center eyebrow contact-eyebrow">Contact us</div>
<div class="abs center script contact-title">For The Further Information</div>
<div class="abs field" style="top:2895px;left:88px;width:504px;height:53px">Write your first name</div>
<div class="abs field" style="top:2895px;left:608px;width:504px;height:53px">Write your last name</div>
<div class="abs field" style="top:2962px;left:88px;width:504px;height:54px">Write your email</div>
<div class="abs field" style="top:2962px;left:608px;width:504px;height:54px">Write your phone number</div>
<div class="abs field field-area" style="top:3030px;left:88px;width:1024px;height:73px">Write your message</div>
<div class="abs btn btn-petrol send-btn">Send</div>

<!-- footer -->
<footer class="abs footer"></footer>
<div class="abs badge" role="img" aria-label="Membership badge"></div>
<div class="abs f-head" style="left:276px">Contact Us</div>
<div class="abs f-list" style="top:3316px;left:276px">Marktstrasse 18 82031 Auenfeld<br>info@corebalance-studio.com<br>+49 170 5512864</div>
<div class="abs f-head" style="left:579px">Quick Links</div>
<div class="abs f-list" style="top:3316px;left:579px">Home<br>Individual Training<br>Group Training<br>About Us<br>Contact Us</div>
<div class="abs f-head" style="left:758px">Subscribe for More Updates</div>
<div class="abs f-input">Write your email</div>
<div class="abs btn btn-petrol f-btn">Subscribe</div>
<div class="abs f-rule"></div>
<div class="abs copy">© Copyright Core Balance | Pilates Glossary | Privacy Policy | Imprint</div>
<div class="abs social" style="left:1013px"></div>
<div class="abs social" style="left:1047px"></div>
<div class="abs social" style="left:1082px"></div>

</body>
</html>
```